Business Card for Dental Office

Our office is in the Hillcrest section of San Diego, California which is a well-established area. Maybe the back can be a map of our office location

```html
<!DOCTYPE html>
<html lang="en">
<head>
<meta charset="utf-8">
<title>Canyon Row Dental – Business Card</title>
<link rel="stylesheet" href="https://fonts.googleapis.com/css2?family=Tinos:wght@400;700&display=swap">
<style>
  :root {
    --backdrop: #ecebe8;
    --card-front: #ffffff;
    --card-back: #d1d1d1;
    --ink: #1a1a1a;
    --ink-soft: #2e2e2e;
    --mark-faint: #e4e4e4;
    --mark-back: #ededed;
    --card-shadow: rgba(0, 0, 0, 0.12);
  }
  * { margin: 0; padding: 0; box-sizing: border-box; }
  html, body {
    width: 1200px;
    height: 900px;
    overflow: hidden;
    background: var(--backdrop);
    font-family: "Tinos", "Times New Roman", serif;
  }
  .canvas {
    width: 1200px;
    height: 900px;
    display: flex;
    flex-direction: column;
    align-items: center;
    justify-content: center;
    gap: 60px;
  }
  .card {
    position: relative;
    width: 560px;
    height: 320px;
    box-shadow: 0 6px 18px var(--card-shadow);
    overflow: hidden;
  }
  .card--front { background: var(--card-front); }
  .card--back {
    background: var(--card-back);
    display: flex;
    align-items: center;
    justify-content: center;
  }
  .front-watermark {
    position: absolute;
    top: 96px;
    right: 28px;
    font-size: 30px;
    line-height: 1;
    color: var(--mark-faint);
    white-space: nowrap;
  }
  .contact {
    position: absolute;
    top: 28px;
    left: 26px;
    color: var(--ink);
    line-height: 1.15;
  }
  .contact__name { font-size: 21px; font-weight: 400; }
  .contact__title { font-size: 15px; color: var(--ink-soft); margin-bottom: 6px; }
  .contact__line { font-size: 15px; color: var(--ink-soft); }
  .front-brand {
    position: absolute;
    right: 18px;
    bottom: 16px;
    display: flex;
    align-items: center;
    gap: 6px;
    font-size: 13px;
    color: var(--ink);
  }
  .front-brand__dot {
    width: 10px;
    height: 10px;
    border-radius: 50%;
    background: var(--ink);
  }
  .back-brand {
    display: flex;
    align-items: center;
    gap: 14px;
    font-size: 36px;
    color: var(--mark-back);
  }
  .back-brand__dot {
    width: 22px;
    height: 22px;
    border-radius: 50%;
    background: var(--mark-back);
  }
</style>
</head>
<body>
  <main class="canvas">
    <section class="card card--front" aria-label="Business card front">
      <div class="front-watermark" aria-hidden="true">Canyon Row Dental</div>
      <div class="contact">
        <p class="contact__name">John Doe</p>
        <p class="contact__title">Chief Executive Officer</p>
        <p class="contact__line">Suite 5, 89 Sample Street</p>
        <p class="contact__line">Singapore</p>
        <p class="contact__line">Phone: 123 456 789</p>
        <p class="contact__line">Cell: 1234 567 89</p>
        <p class="contact__line">Email: yourname@yourcompany.com</p>
      </div>
      <div class="front-brand">
        <span class="front-brand__dot"></span>
        <span>Canyon Row Dental</span>
      </div>
    </section>

    <section class="card card--back" aria-label="Business card back">
      <div class="back-brand">
        <span class="back-brand__dot"></span>
        <span>Canyon Row Dental</span>
      </div>
    </section>
  </main>
</body>
</html>
```